New Company Business Card Design

I have a new company logo and I want a new business card design. I dont know if the logo file i attached is in the correct format or quality. We are a New York City Specialty construction Firm specializing in high risk out of the box projects. I want a simple and classy business card that people will his card is as crisp as the work his company does.

Target Market(s)

Clients in the heavy construction industry in New York City

Industry/Entity Type

Construction Company

Contact Information for Business Card

Simple Classy - DIFFERENT

Font styles to use
Other font styles liked:
• Mach the logo font in some way

Colors

Designer to choose colors to be used in the design.

Requirements
Must have
• Uniqueness
Nice to have
• Nothing particular - Just different and classy - Timeless
Should not have
• Goofy Shit or Gimmicky shit

```html
<!DOCTYPE html>
<html lang="en">
<head>
<meta charset="utf-8">
<title>Ridgeline Associates – Business Card</title>
<link rel="stylesheet" href="https://fonts.googleapis.com/css2?family=Open+Sans:wght@400;600;800&display=swap">
<style>
  :root {
    --bg: #d9d9d9;
    --card: #ffffff;
    --ink: #111111;
    --blue: #1f6fc0;
    --blue-deep: #114a96;
    --icon: #2f6f98;
    --shadow: rgba(0,0,0,0.18);
  }
  * { margin: 0; padding: 0; box-sizing: border-box; }
  html, body { width: 1200px; height: 864px; overflow: hidden; }
  body {
    background: var(--bg);
    font-family: "Open Sans", sans-serif;
    color: var(--ink);
    position: relative;
  }
  .card {
    position: absolute;
    width: 600px;
    height: 343px;
    background: var(--card);
    box-shadow: 0 6px 18px var(--shadow);
    overflow: hidden;
  }
  .card--back { left: 300px; top: 50px; }
  .card--front { left: 300px; top: 440px; }

  .back-name {
    position: absolute;
    left: 0; right: 0; top: 150px;
    text-align: center;
    font-weight: 800;
    font-size: 22px;
    letter-spacing: 1px;
    color: var(--ink);
  }

  .brand {
    position: absolute;
    left: 28px; top: 28px;
    display: flex; align-items: center; gap: 10px;
  }
  .brand-mark { width: 16px; height: 16px; background: var(--blue); }
  .brand-name {
    font-weight: 800;
    font-size: 26px;
    line-height: 1;
    color: var(--blue);
  }

  .contacts {
    position: absolute;
    left: 26px; top: 82px;
    list-style: none;
  }
  .contacts li {
    display: flex; align-items: center; gap: 10px;
    height: 21px;
    font-size: 14.5px;
  }
  .contacts svg { width: 13px; height: 13px; flex: none; }

  .person {
    position: absolute;
    left: 430px; top: 176px;
  }
  .person-name { font-size: 20px; font-weight: 600; line-height: 1.1; }
  .person-role { font-size: 15px; }

  .swoosh { position: absolute; inset: 0; width: 600px; height: 343px; }
</style>
</head>
<body>

  <section class="card card--back" aria-label="Card back">
    <p class="back-name">Ridgeline Associates, Inc.</p>
  </section>

  <section class="card card--front" aria-label="Card front">
    <svg class="swoosh" viewBox="0 0 600 343" aria-hidden="true">
      <defs>
        <linearGradient id="waveBlue" x1="0" y1="0" x2="1" y2="0">
          <stop offset="0" stop-color="#3d8ad6"/>
          <stop offset="1" stop-color="#0f4f9e"/>
        </linearGradient>
      </defs>
      <path d="M0 196 C 120 290, 360 300, 600 286 L600 296 C 360 314, 120 306, 0 222 Z" fill="var(--ink)"/>
      <path d="M240 312 C 390 318, 500 310, 600 302 L600 343 L330 343 C 300 330, 270 320, 240 312 Z" fill="url(#waveBlue)"/>
    </svg>

    <div class="brand">
      <span class="brand-name">Ridgeline Associates, Inc.</span>
    </div>

    <ul class="contacts">
      <li>
        <svg viewBox="0 0 14 14"><rect x="3.5" y="1" width="7" height="12" rx="1.2" fill="none" stroke="var(--icon)" stroke-width="1.4"/><circle cx="7" cy="11" r="0.8" fill="var(--icon)"/></svg>
        +01 555 010 742
      </li>
      <li>
        <svg viewBox="0 0 14 14"><path d="M3 1.5 L5.5 1.5 L6.3 4.5 L4.8 5.6 C5.6 7.4 6.7 8.5 8.4 9.3 L9.5 7.8 L12.5 8.6 L12.5 11 C12.5 12 11.6 12.6 10.6 12.4 C6 11.5 2.6 8 1.7 3.4 C1.5 2.4 2.1 1.5 3 1.5 Z" fill="var(--icon)"/></svg>
        +01 555 010 742
      </li>
      <li>
        <svg viewBox="0 0 14 14"><rect x="1" y="3" width="12" height="8.5" fill="var(--icon)"/><path d="M1 3 L7 8 L13 3" fill="none" stroke="#fff" stroke-width="1.1"/></svg>
        info@ridgelineinc.com
      </li>
      <li>
        <svg viewBox="0 0 14 14"><circle cx="7" cy="7" r="5.8" fill="none" stroke="var(--icon)" stroke-width="1.3"/><ellipse cx="7" cy="7" rx="2.6" ry="5.8" fill="none" stroke="var(--icon)" stroke-width="1"/><path d="M1.2 7 H12.8 M2 4 H12 M2 10 H12" stroke="var(--icon)" stroke-width="0.9"/></svg>
        www.ridgelineinc.com
      </li>
      <li>
        <svg viewBox="0 0 14 14"><path d="M7 13 C 4 9, 2.5 7, 2.5 5 A4.5 4.5 0 0 1 11.5 5 C11.5 7, 10 9, 7 13 Z" fill="var(--icon)"/><circle cx="7" cy="5" r="1.6" fill="#fff"/></svg>
        2270 Harbor View Road, Port Orchard, Ohio, 43210
      </li>
    </ul>

    <div class="person">
      <p class="person-name">Daniel Marsh</p>
      <p class="person-role">Manager</p>
    </div>
  </section>

</body>
</html>
```